Safety training business card design

We need a buisness card design and logo for a small buisness that provides safety training through out the mining and civil construction industries. We provide first aid , confined space working at heights , machinery tickets, chainsaw, four wheel drive and four wheel motorbike training. We would like to use the design colors of navy blue, Fluro or lime green and white .

Industry/Entity Type

Construction

Contact Information for Business Card

Kelbrook Earthmoving & Training , Dennis Holloway, kelbrook.training@mailbox-example.com, ph 0438615044 abn 47 816 305 971

```html
<!DOCTYPE html>
<html lang="en">
<head>
<meta charset="utf-8">
<title>Kelbrook Earthmoving &amp; Training — Business Card</title>
<link href="https://fonts.googleapis.com/css2?family=Fira+Sans:ital,wght@0,400;0,500;0,700;1,400&display=swap" rel="stylesheet">
<style>
  :root {
    --bg: #e9ecef;
    --brand-blue: #0b5ca3;
    --navy: #1b3f8e;
    --lime: #a9c23a;
    --white: #ffffff;
  }
  * { box-sizing: border-box; margin: 0; padding: 0; }
  html, body { width: 1200px; height: 926px; overflow: hidden; }
  body {
    background: var(--bg);
    font-family: "Fira Sans", Arial, sans-serif;
    display: flex;
    align-items: center;
    justify-content: center;
    gap: 60px;
  }
  .card {
    position: relative;
    width: 540px;
    height: 320px;
    overflow: hidden;
    box-shadow: 0 2px 10px rgba(0,0,0,0.12);
  }

  /* Front */
  .card--front { background: var(--white); }
  .brand {
    position: absolute;
    top: 58px;
    left: 0; right: 0;
    display: flex;
    justify-content: center;
    align-items: center;
    gap: 16px;
  }
  .brand__mark {
    width: 18px; height: 18px;
    border-radius: 50%;
    background: var(--brand-blue);
  }
  .brand__divider {
    width: 2px; height: 74px;
    background: var(--lime);
  }
  .brand__name {
    color: var(--brand-blue);
    font-weight: 500;
    font-size: 21px;
    line-height: 1.05;
    text-transform: uppercase;
  }
  .name-band {
    position: absolute;
    top: 170px; left: 0; right: 0;
    height: 36px;
    background: var(--lime);
    border-bottom: 4px solid var(--white);
    box-sizing: content-box;
  }
  .name-band__name {
    position: absolute;
    left: 0; right: 0;
    top: 4px;
    text-align: center;
    color: var(--navy);
    font-weight: 700;
    font-size: 22px;
    letter-spacing: 0.5px;
  }
  .contact-panel {
    position: absolute;
    top: 210px; left: 0; right: 0; bottom: 0;
    background: var(--brand-blue);
    padding: 20px 0 0 48px;
    color: var(--white);
    font-size: 17px;
    line-height: 1.65;
  }
  .contact-panel__label {
    color: var(--lime);
    font-style: italic;
  }

  /* Back */
  .card--back {
    background: var(--brand-blue);
    color: var(--white);
    text-align: center;
  }
  .back-brand {
    position: absolute;
    top: 62px; left: 0; right: 0;
    display: flex;
    justify-content: center;
    align-items: center;
    gap: 12px;
  }
  .back-brand__mark {
    width: 16px; height: 16px;
    border-radius: 50%;
    background: var(--white);
  }
  .back-brand__name {
    font-weight: 500;
    font-size: 20px;
    text-transform: uppercase;
  }
  .services__title {
    position: absolute;
    top: 140px; left: 0; right: 0;
    color: var(--lime);
    font-size: 24px;
    font-weight: 500;
  }
  .services__title strong { font-weight: 700; }
  .services__list {
    position: absolute;
    top: 182px; left: 40px; right: 40px;
    font-size: 14px;
    line-height: 1.3;
    text-transform: uppercase;
    letter-spacing: 0.3px;
  }
</style>
</head>
<body>

  <section class="card card--front">
    <div class="brand">
      <span class="brand__mark"></span>
      <span class="brand__divider"></span>
      <div class="brand__name">Kelbrook<br>Earthmoving &amp;<br>Training</div>
    </div>
    <div class="name-band">
      <p class="name-band__name">Dennis Holloway</p>
    </div>
    <div class="contact-panel">
      <p><span class="contact-panel__label">email:</span> kelbrook.training@mailbox-example.com</p>
      <p><span class="contact-panel__label">phone:</span> 043 861 5044 and 47 816 305 971</p>
    </div>
  </section>

  <section class="card card--back">
    <div class="back-brand">
      <span class="back-brand__mark"></span>
      <span class="back-brand__name">Kelbrook</span>
    </div>
    <h2 class="services__title">WE <strong>PROVIDE</strong></h2>
    <p class="services__list">First aid, confined space working at heights, machinery tickets, chainsaw, four wheel drive and four wheel motorbike training</p>
  </section>

</body>
</html>
```